I need a business card for ALVA Holdings. We are a young startup based in New Zealand working in internet marketing and web development. The design should have some element connected to New Zealand, such as wave, koru or silver fern, just don't use a kiwi bird.

```html
<!DOCTYPE html>
<html lang="en">
<head>
<meta charset="utf-8">
<title>ALVA Holdings – Business Card</title>
<link href="https://fonts.googleapis.com/css2?family=Work+Sans:wght@400;500;700&display=swap" rel="stylesheet">
<style>
  :root {
    --backdrop: #1a1a1a;
    --card: #262626;
    --card-edge: #303030;
    --blue: #1a7bd0;
    --orange: #f0622a;
    --silver: #9a9a9a;
    --text: #f2f2f2;
  }
  * { box-sizing: border-box; margin: 0; padding: 0; }
  html, body {
    width: 1200px; height: 900px; overflow: hidden;
    background: var(--backdrop);
    font-family: "Work Sans", sans-serif;
  }
  .stage {
    width: 1200px; height: 900px;
    display: flex; flex-direction: column; align-items: center; justify-content: center;
    gap: 34px;
  }
  .card {
    width: 700px; height: 400px;
    background: linear-gradient(135deg, var(--card) 0%, var(--card-edge) 100%);
    box-shadow: 0 10px 30px rgba(0,0,0,.55);
    position: relative;
  }
  .card-front { display: flex; align-items: center; justify-content: center; }
  .wordmark { display: flex; align-items: center; gap: 14px; font-weight: 700; letter-spacing: .02em; }
  .wordmark-dot { width: 44px; height: 44px; border-radius: 50%; }
  .card-front .wordmark { font-size: 54px; color: var(--silver); }
  .card-front .wordmark-dot { background: var(--silver); width: 52px; height: 52px; }
  .card-back { display: flex; align-items: center; padding: 0 48px; }
  .card-back .brand { width: 330px; }
  .card-back .wordmark { font-size: 36px; color: var(--blue); }
  .card-back .wordmark-dot { background: var(--blue); width: 36px; height: 36px; }
  .divider { width: 3px; height: 200px; background: var(--blue); margin: 0 36px 0 10px; }
  .contact { color: var(--text); font-size: 17px; line-height: 1.45; }
  .contact-name { color: var(--blue); font-size: 26px; font-weight: 500; letter-spacing: .06em; line-height: 1.1; }
  .contact-role { margin-bottom: 14px; }
  .contact-address { margin-bottom: 12px; }
  .contact-line { display: flex; align-items: center; gap: 10px; }
  .contact-line svg { width: 13px; height: 13px; flex: none; }
  .web-accent { color: var(--orange); }
</style>
</head>
<body>
<main class="stage">
  <section class="card card-front">
    <div class="wordmark"><span>ALVA Holdings</span><span class="wordmark-dot"></span></div>
  </section>

  <section class="card card-back">
    <div class="brand">
      <div class="wordmark"><span>ALVA Holdings</span><span class="wordmark-dot"></span></div>
    </div>
    <div class="divider"></div>
    <div class="contact">
      <p class="contact-name">ROWAN TAIT</p>
      <p class="contact-role">Director</p>
      <p class="contact-address">52 Harbour Lane,<br>Nelson, NZ, 7010</p>
      <p class="contact-line">
        <svg viewBox="0 0 16 16" aria-hidden="true"><path d="M4 1l3 3-2 2c1 2 3 4 5 5l2-2 3 3-2 2C7 14 2 9 2 3z" fill="var(--blue)"/></svg>
        (555) 210-4478
      </p>
      <p class="contact-line">
        <svg viewBox="0 0 16 16" aria-hidden="true"><rect x="1.5" y="3.5" width="13" height="9" fill="none" stroke="var(--blue)" stroke-width="1.5"/><path d="M1.5 3.5l6.5 5 6.5-5" fill="none" stroke="var(--blue)" stroke-width="1.5"/></svg>
        info@alvaholdings.com
      </p>
      <p class="contact-line">
        <svg viewBox="0 0 16 16" aria-hidden="true"><circle cx="8" cy="8" r="6.5" fill="none" stroke="var(--blue)" stroke-width="1.5"/><path d="M1.5 8h13M8 1.5c-3 3.5-3 9.5 0 13M8 1.5c3 3.5 3 9.5 0 13" fill="none" stroke="var(--blue)" stroke-width="1.2"/></svg>
        <span>www.<span class="web-accent">alvaholdings</span>.com</span>
      </p>
    </div>
  </section>
</main>
</body>
</html>
```